Mindfulness School for Children -- Business Cards

We're looking for business cards for our school directors and owners. We're a mindfulness school for children called little compass. Attached are our logos/icons.

```html
<!DOCTYPE html>
<html lang="en">
<head>
<meta charset="UTF-8">
<title>little compass — Business Cards</title>
<link href="https://fonts.googleapis.com/css2?family=Work+Sans:wght@400;500;600&display=swap" rel="stylesheet">
<style>
  :root {
    --backdrop: #a8a8a8;
    --card-white: #ffffff;
    --card-dark: #2c2c2c;
    --teal: #3fa3c4;
    --sage: #6cc19a;
    --ink: #3a3a3a;
    --rule: #7cc4d6;
  }
  * { margin: 0; padding: 0; box-sizing: border-box; }
  html, body {
    width: 1200px; height: 800px; overflow: hidden;
    background: var(--backdrop);
    font-family: "Work Sans", Arial, sans-serif;
  }
  .stage {
    position: relative; width: 1200px; height: 800px;
  }
  .card {
    position: absolute; top: 245px;
    width: 540px; height: 309px;
    box-shadow: 0 10px 28px rgba(0,0,0,0.25);
  }
  .card--front { left: 40px; background: var(--card-white); }
  .card--back {
    left: 620px; background: var(--card-dark);
    display: flex; align-items: center; justify-content: center;
  }

  /* front */
  .brand-mark {
    position: absolute; top: 26px; right: 30px;
    display: flex; align-items: center; gap: 7px;
    color: var(--teal); font-size: 13px; font-weight: 500;
  }
  .brand-mark__dot {
    width: 14px; height: 14px; border-radius: 50%; background: var(--teal);
  }
  .identity {
    position: absolute; left: 40px; top: 118px; width: 190px;
    text-align: right;
  }
  .identity__name {
    color: var(--teal); font-size: 19px; font-weight: 600;
    letter-spacing: 0.5px; text-transform: uppercase;
  }
  .identity__role {
    color: var(--sage); font-size: 13px; margin-top: 2px;
  }
  .divider {
    position: absolute; left: 248px; top: 98px;
    width: 1px; height: 94px; background: var(--rule);
  }
  .contact {
    position: absolute; left: 264px; top: 96px;
    list-style: none; color: var(--ink); font-size: 12.5px; line-height: 17px;
  }
  .contact__item { display: flex; align-items: flex-start; gap: 8px; }
  .contact__icon { width: 11px; height: 11px; margin-top: 3px; flex: none; }
  .website {
    position: absolute; left: 0; right: 0; bottom: 36px;
    text-align: center; color: var(--ink); font-size: 12.5px;
    letter-spacing: 4px;
  }

  /* back */
  .wordmark {
    color: var(--sage); font-size: 50px; font-weight: 500;
    letter-spacing: 0.5px;
  }
</style>
</head>
<body>
<main class="stage">
  <section class="card card--front" aria-label="Business card, front">
    <div class="brand-mark"><span class="brand-mark__dot"></span>little compass</div>

    <div class="identity">
      <p class="identity__name">Daniel Reyes</p>
      <p class="identity__role">President</p>
    </div>
    <div class="divider"></div>

    <ul class="contact">
      <li class="contact__item">
        <svg class="contact__icon" viewBox="0 0 12 12"><path d="M6 0.5a4 4 0 0 0-4 4c0 3 4 7 4 7s4-4 4-7a4 4 0 0 0-4-4z" fill="#6cc19a"/><circle cx="6" cy="4.5" r="1.5" fill="#fff"/></svg>
        <span>4120 Willowbrook Road<br>Fairview, Oregon 97024</span>
      </li>
      <li class="contact__item">
        <svg class="contact__icon" viewBox="0 0 12 12"><path d="M2.5 1l2 2.5-1.2 1.3c.8 1.7 2.2 3 3.9 3.9l1.3-1.2L11 9.5 9.5 11C5 10.5 1.5 7 1 2.5z" fill="#6cc19a"/></svg>
        <span>555-214-7730</span>
      </li>
      <li class="contact__item">
        <svg class="contact__icon" viewBox="0 0 12 12"><rect x="2.5" y="0.5" width="7" height="11" rx="1.2" fill="none" stroke="#6cc19a" stroke-width="1.2"/></svg>
        <span>555-309-6142</span>
      </li>
      <li class="contact__item">
        <svg class="contact__icon" viewBox="0 0 12 12"><rect x="0.5" y="0.5" width="11" height="11" rx="1.5" fill="#6cc19a"/><path d="M3 6.2l2 2 4-4.4" fill="none" stroke="#fff" stroke-width="1.4"/></svg>
        <span>name@littlecompass.com</span>
      </li>
    </ul>

    <p class="website">www.littlecompass.com</p>
  </section>

  <section class="card card--back" aria-label="Business card, back">
    <p class="wordmark">littlecompass</p>
  </section>
</main>
</body>
</html>
```